Business Card Design

I would like a new business card design for an accounting firm that specializes in resolving clients tax problems. I want the card to give the impression that we are not your typical stodgy accounting firm, but at the same time we will get the job done.
Industry/Entity Type
Business
Contact Information for Business Card
Dorian T Welsby
Certified Public Accountant
38-27 52nd Street
Sunnyside, NY 11287
Tel: (718) 555-0142
Fax: (888) 555-0199
e-mail: dtwthecpa@ledgerpost.com
website: harborfilingreliefexperts.com

```html
<!DOCTYPE html>
<html lang="en">
<head>
<meta charset="utf-8">
<title>Dorian T Welsby, CPA — Business Card</title>
<link rel="stylesheet" href="https://fonts.googleapis.com/css2?family=Roboto:wght@400;500;700&display=swap">
<style>
  :root {
    --backdrop: #3b3b3d;
    --card-white: #f4f4f4;
    --card-white-shade: #e2e2e2;
    --navy: #1d467f;
    --gold: #e8b21c;
    --ink-light: #ffffff;
    --ink-navy: #1d3f74;
  }
  * { box-sizing: border-box; margin: 0; padding: 0; }
  html, body {
    width: 1200px;
    height: 900px;
    overflow: hidden;
    background: var(--backdrop);
    font-family: "Roboto", Arial, sans-serif;
  }
  .canvas {
    width: 1200px;
    height: 900px;
    display: flex;
    align-items: center;
    justify-content: center;
  }
  .business-card {
    position: relative;
    width: 1000px;
    height: 572px;
    border-radius: 26px;
    overflow: hidden;
    display: flex;
    box-shadow: 0 18px 40px rgba(0,0,0,0.45);
  }
  .brand-side {
    width: 400px;
    height: 100%;
    background: linear-gradient(160deg, var(--card-white) 0%, var(--card-white) 55%, var(--card-white-shade) 100%);
    display: flex;
    align-items: center;
    justify-content: center;
    padding-bottom: 70px;
  }
  .brand-mark {
    display: flex;
    align-items: center;
    gap: 14px;
  }
  .brand-square {
    width: 22px;
    height: 22px;
    background: var(--navy);
  }
  .brand-name {
    font-size: 38px;
    font-weight: 700;
    color: var(--ink-navy);
    letter-spacing: 0.5px;
  }
  .divider-stripe {
    width: 7px;
    height: 100%;
    background: var(--gold);
  }
  .contact-side {
    position: relative;
    flex: 1;
    background: var(--navy);
    color: var(--ink-light);
  }
  .holder-name {
    position: absolute;
    left: 130px;
    top: 110px;
    font-size: 44px;
    font-weight: 400;
    letter-spacing: 0.3px;
  }
  .holder-credential {
    font-size: 22px;
    margin-left: 4px;
  }
  .name-rule {
    position: absolute;
    left: 60px;
    top: 196px;
    width: 470px;
    height: 3px;
    background: linear-gradient(90deg, rgba(232,178,28,0) 0%, var(--gold) 40%, rgba(232,178,28,0) 100%);
  }
  .contact-list {
    position: absolute;
    left: 50px;
    top: 238px;
    list-style: none;
    font-size: 25px;
    line-height: 1.2;
  }
  .contact-item {
    display: flex;
    align-items: flex-start;
    gap: 16px;
    margin-bottom: 10px;
  }
  .contact-icon {
    width: 26px;
    height: 26px;
    flex: none;
    margin-top: 2px;
  }
  .contact-web {
    margin-top: 6px;
    padding-left: 42px;
  }
</style>
</head>
<body>
<main class="canvas">
  <article class="business-card">
    <section class="brand-side">
      <div class="brand-mark">
        <span class="brand-square"></span>
        <span class="brand-name">Dorian T Welsby</span>
      </div>
    </section>
    <div class="divider-stripe"></div>
    <section class="contact-side">
      <h1 class="holder-name">Dorian T Welsby, <span class="holder-credential">CPA</span></h1>
      <div class="name-rule"></div>
      <ul class="contact-list">
        <li class="contact-item">
          <svg class="contact-icon" viewBox="0 0 26 26" aria-hidden="true">
            <circle cx="13" cy="13" r="12" fill="var(--gold)"/>
            <path d="M9 7c1 0 2 2.5 2 3s-1.2 1-1 1.8c.5 1.6 2 3.2 3.6 3.7.8.2 1.2-1 1.8-1s3 1 3 2-1.5 2.5-3 2.3C10.5 18 7.5 14.5 7 10.5 6.8 8.8 8 7 9 7z" fill="var(--navy)"/>
          </svg>
          <span>(718) 555-0142</span>
        </li>
        <li class="contact-item">
          <svg class="contact-icon" viewBox="0 0 26 26" aria-hidden="true">
            <rect x="7" y="3" width="12" height="7" fill="var(--gold)"/>
            <rect x="3" y="10" width="20" height="10" rx="2" fill="var(--gold)"/>
            <rect x="7" y="16" width="12" height="7" fill="var(--gold)" stroke="var(--navy)" stroke-width="1.5"/>
          </svg>
          <span>(888) 555-0199</span>
        </li>
        <li class="contact-item">
          <svg class="contact-icon" viewBox="0 0 26 26" aria-hidden="true">
            <rect x="2" y="6" width="22" height="15" fill="none" stroke="var(--gold)" stroke-width="2"/>
            <path d="M2 6l11 9 11-9" fill="none" stroke="var(--gold)" stroke-width="2"/>
          </svg>
          <span>dtwthecpa@ledgerpost.com</span>
        </li>
        <li class="contact-item">
          <svg class="contact-icon" viewBox="0 0 26 26" aria-hidden="true">
            <path d="M13 2a7.5 7.5 0 0 0-7.5 7.5C5.5 15 13 24 13 24s7.5-9 7.5-14.5A7.5 7.5 0 0 0 13 2z" fill="var(--gold)"/>
            <circle cx="13" cy="9.5" r="3" fill="var(--navy)"/>
          </svg>
          <span>38-27 52nd Street<br>Sunnyside, NY 11287</span>
        </li>
        <li class="contact-item">
          <svg class="contact-icon" viewBox="0 0 26 26" aria-hidden="true">
            <circle cx="13" cy="13" r="11" fill="none" stroke="var(--gold)" stroke-width="2"/>
            <ellipse cx="13" cy="13" rx="5" ry="11" fill="none" stroke="var(--gold)" stroke-width="1.6"/>
            <path d="M2 13h22M4 7.5h18M4 18.5h18" stroke="var(--gold)" stroke-width="1.6"/>
          </svg>
          <span>harborfilingreliefexperts.com</span>
        </li>
      </ul>
    </section>
  </article>
</main>
</body>
</html>
```